TROVEL Industrial Maintenance

I offer repair and maintenance services of industrial mechanics in Quebec. I would like a creation that reflects confidence, competence, professionalism and dynamism. I like the orange color and the blue color.

Target Market(s)

Industries and Manufacturing companies using industrial machinery for the manufacture of their products.

Industry/Entity Type

Manufacturing

Contact Information for Business Card

TROVEL Maintenance Industrielle
Tél: (450)-317-5826
Courriel: trovel.mnt@brixomail.com

Font styles to use
Sans Serif

Colors
f78f20
0455a3

Requirements
Must have
• My company name: TROVEL Maintenance Industrielle My phone: (450) -317-5826 My email: trovel.mnt@brixomail.com
Nice to have
• Integrate a representative logo of the mechanics (gears, mechanical parts)

```html
<!DOCTYPE html>
<html lang="fr">
<head>
<meta charset="utf-8">
<title>TROVEL Maintenance Industrielle – Business Card</title>
<link href="https://fonts.googleapis.com/css2?family=Lato:wght@400;700;900&display=swap" rel="stylesheet">
<style>
  :root {
    --brand-blue: #0455a3;
    --brand-orange: #f78f20;
    --card-light: #f1f3f6;
    --card-white: #ffffff;
    --backdrop: #e4e7eb;
    --text-light: #ffffff;
  }
  * { margin: 0; padding: 0; box-sizing: border-box; }
  html, body {
    width: 1200px;
    height: 900px;
    overflow: hidden;
    background: var(--backdrop);
    font-family: "Lato", Arial, sans-serif;
  }
  .business-card {
    position: absolute;
    left: 160px;
    top: 177px;
    width: 880px;
    height: 546px;
    filter: drop-shadow(0 10px 24px rgba(0, 0, 0, 0.18));
  }
  .card-shape {
    position: absolute;
    inset: 0;
    overflow: visible;
  }
  .holder-name {
    position: absolute;
    left: 50px;
    top: 44px;
    color: var(--text-light);
    font-weight: 700;
    font-size: 33px;
    letter-spacing: 0.5px;
  }
  .holder-role {
    position: absolute;
    left: 51px;
    top: 91px;
    color: var(--text-light);
    font-weight: 400;
    font-size: 23px;
  }
  .contact-list {
    position: absolute;
    left: 50px;
    top: 432px;
    list-style: none;
    color: var(--text-light);
    font-size: 24px;
    line-height: 34px;
  }
  .contact-list li {
    display: flex;
    align-items: center;
    gap: 6px;
  }
  .contact-icon {
    width: 20px;
    height: 20px;
    fill: var(--text-light);
  }
  .company-mark {
    position: absolute;
    left: 392px;
    top: 215px;
    width: 440px;
    display: flex;
    align-items: center;
    gap: 14px;
  }
  .mark-dot {
    flex: none;
    width: 34px;
    height: 34px;
    border-radius: 50%;
    background: var(--brand-orange);
  }
  .company-name {
    color: var(--brand-blue);
    font-weight: 900;
    line-height: 1;
  }
  .company-name .name-main {
    display: block;
    font-size: 78px;
    letter-spacing: 3px;
  }
  .company-name .name-sub {
    display: block;
    font-size: 23px;
    letter-spacing: 0.5px;
    margin-top: 6px;
    text-transform: uppercase;
  }
</style>
</head>
<body>
  <div class="business-card">
    <svg class="card-shape" width="880" height="546" viewBox="0 0 880 546" aria-hidden="true">
      <!-- card body: square left end, fully rounded right end -->
      <path d="M6 0 H607 A273 273 0 0 1 607 546 H6 A6 6 0 0 1 0 540 V6 A6 6 0 0 1 6 0 Z" fill="var(--card-light)"/>
      <!-- top band -->
      <path d="M6 0 H607 V176 H0 V6 A6 6 0 0 1 6 0 Z" fill="var(--brand-blue)"/>
      <!-- bottom band -->
      <path d="M0 370 H607 V546 H6 A6 6 0 0 1 0 540 Z" fill="var(--brand-blue)"/>
      <!-- logo disc with ring, forming the rounded end -->
      <circle cx="607" cy="273" r="273" fill="var(--brand-blue)"/>
      <circle cx="607" cy="273" r="265" fill="var(--card-white)"/>
    </svg>

    <div class="holder-name">JULIEN MARCHAND</div>
    <div class="holder-role">Managing Director</div>

    <div class="company-mark">
      <span class="mark-dot"></span>
      <div class="company-name">
        <span class="name-main">TROVEL</span>
        <span class="name-sub">Maintenance Industrielle</span>
      </div>
    </div>

    <ul class="contact-list">
      <li>
        <svg class="contact-icon" viewBox="0 0 24 24" aria-hidden="true">
          <path d="M3 9c0-3 4-5 9-5s9 2 9 5v1.5h-4.5V8.5c-1.4-.6-3-.9-4.5-.9s-3.1.3-4.5.9v2H3zM6 12h12l2 7H4zm6 1.8a2.4 2.4 0 1 0 0 4.8 2.4 2.4 0 0 0 0-4.8z"/>
        </svg>
        <span>(450) -317-5826</span>
      </li>
      <li>
        <svg class="contact-icon" viewBox="0 0 24 24" aria-hidden="true">
          <path d="M3 5h18v14H3zm2 2v.4l7 5 7-5V7zm0 2.8V17h14V9.8l-7 5z"/>
        </svg>
        <span>trovel.mnt@brixomail.com</span>
      </li>
    </ul>
  </div>
</body>
</html>
```